Larkspur Ridge Management - Business Cards

I need business cards. My current logo was designed by a designer at this site and I very much like and am happy with the results. I would like a business card that is trendy, unique, current yet professional. I deal with high net worth clients daily

Target Market(s)

Out of state investors looking to get into the rental market in Ohio

Industry/Entity Type

Property Management, Consulting

Contact Information for Business Card

Name, Title (Chief Financial Officer) office phone number (555) 817-3094 website address larkridgemgmt.example

Font styles to use
Sans Serif

Colors
0054AA
0677BA
7BADD7
CADEEF
E8F1F8
0094D4
00A9DD
6FCCEA
C7EBF8
E9F6FB
00AB8E
00BBA5
67D7C9
C6EFE9
E9F9F6

```html
<!DOCTYPE html>
<html lang="en">
<head>
<meta charset="utf-8">
<title>Larkspur Ridge Management – Business Cards</title>
<link href="https://fonts.googleapis.com/css2?family=Montserrat:wght@400;700;800&display=swap" rel="stylesheet">
<style>
  :root {
    --backdrop: #c2c2c2;
    --card: #ffffff;
    --navy: #2a3d66;
    --red: #c1272d;
    --ink: #555a60;
  }
  * { box-sizing: border-box; margin: 0; padding: 0; }
  html, body {
    width: 1200px; height: 1200px; overflow: hidden;
    background: var(--backdrop);
    font-family: "Montserrat", Arial, sans-serif;
  }
  .canvas { position: relative; width: 1200px; height: 1200px; }
  .card {
    position: absolute; left: 239px; width: 722px; height: 410px;
    background: var(--card); border-radius: 25px; overflow: hidden;
  }
  .card--front { top: 149px; }
  .card--back { top: 645px; }

  .brand-mark {
    position: absolute; color: var(--navy); font-weight: 800;
    text-transform: uppercase; text-align: center; line-height: 1.1;
  }
  .card--front .brand-mark {
    right: 62px; top: 64px; width: 150px; font-size: 17px;
  }
  .card--back .brand-mark {
    left: 0; right: 0; top: 150px; font-size: 44px; letter-spacing: 1px;
  }
  .brand-mark .brand-sub { display: block; font-size: 0.55em; letter-spacing: 2px; margin-top: 6px; }

  .person { position: absolute; left: 62px; top: 196px; }
  .person-name { color: var(--navy); font-weight: 700; font-size: 26px; letter-spacing: 0.5px; }
  .person-title { color: var(--ink); font-weight: 400; font-size: 19px; letter-spacing: 0.6px; margin-top: 2px; }

  .divider { position: absolute; left: 62px; right: 62px; top: 261px; height: 2px; background: var(--red); }

  .contacts { position: absolute; left: 62px; top: 274px; list-style: none; }
  .contacts li {
    display: flex; align-items: center; height: 27px;
    font-size: 19px; color: var(--ink); letter-spacing: 0.4px;
  }
  .contacts svg { width: 16px; height: 16px; margin-right: 9px; fill: var(--navy); flex: none; }
  .contacts .accent { color: var(--red); }

  .address {
    position: absolute; right: 62px; top: 276px; text-align: right;
    font-size: 19px; line-height: 26px; color: var(--ink); letter-spacing: 0.4px;
    font-style: normal;
  }
</style>
</head>
<body>
<main class="canvas">
  <section class="card card--front">
    <div class="brand-mark">Larkspur Ridge<span class="brand-sub">Management</span></div>

    <div class="person">
      <h1 class="person-name">DANIEL HARTWELL</h1>
      <p class="person-title">Chief Financial Officer</p>
    </div>

    <div class="divider"></div>

    <ul class="contacts">
      <li>
        <svg viewBox="0 0 16 16" aria-hidden="true"><path d="M3.5 1.5l2.2 2.8-1.3 1.6c.9 2 2.6 3.7 4.6 4.6l1.6-1.3 2.8 2.2-1.4 2.3C6.8 13.3 2.7 9.2 1.2 3z"/></svg>
        (555) 817-3094
      </li>
      <li>
        <svg viewBox="0 0 16 16" aria-hidden="true"><path d="M1 3h14v1.2L8 8.6 1 4.2z M1 6l7 4.4L15 6v7H1z"/></svg>
        daniel@larkridgemgmt.example
      </li>
      <li>
        <svg viewBox="0 0 16 16" aria-hidden="true"><circle cx="8" cy="8" r="7"/><path d="M4 5c2 0 2 2 4 2s1 3-1 3-1 3-2 3c-1-2-2-4-1-8z M10 3c2 1 3 3 3 5-1 0-2-1-3-1s-1-2 0-4z" fill="#fff"/></svg>
        <span>www.<span class="accent">larkridgemgmt</span>.example</span>
      </li>
    </ul>

    <address class="address">
      4150 Orchard Crest Rd<br>
      Fairbrook, Ohio(OH),<br>
      45999
    </address>
  </section>

  <section class="card card--back">
    <div class="brand-mark">Larkspur Ridge<span class="brand-sub">Management</span></div>
  </section>
</main>
</body>
</html>
```